'Private English tutoring'

I need a flyer design to advertise private English tutoring. I am offering lessons to ethnic minority groups in my local area in south Belfast. The biggest ethnic minorities groups are Chinese, Polish and Indian and African. I can teach at any level, from beginner English to advanced. The tutoring will be either one on one or small groups of four students. I can teach adults and children but my preference would be to teach adults.

The flyer would need to be easily understood by people who have English as a second language.

I am also offering proof reading and editing services to students at local universities and colleges.

Target Market(s)

Adults of ethnic minorities who may not speak or read much English

Industry/Entity Type

Tutoring

Font styles to use
Serif

Requirements
Must have
• It needs to communicate that I am an accredited TEFL (Teaching English as a Foreign language) tutor with 2 years experience and that I tutor Beginners - Advanced students. It would also need to say that I offer proof reading and editing services. It would also need to communicate the cost of lessons are £15, but there are group rates for groups of 2-4 students. It would need to include my contact details which are as follows: contact Mona Hargrove BTh at 07812609354 or email monahargroveenglish@quillpost.com
Nice to have
• In terms of design I would like it to be warm and inviting and something which would convey an atmosphere of learning for non English speakers. Other than that I don't have any preferences.
Should not have
• Nothing which is going to be offensive to ethnic minorities.
• No pictures of people

```html
<!DOCTYPE html>
<html lang="en">
<head>
<meta charset="utf-8">
<title>English Tutoring – Private English Classes</title>
<link rel="stylesheet" href="https://fonts.googleapis.com/css2?family=Cabin+Sketch:wght@400;700&family=Delius&display=swap">
<style>
  :root {
    --maroon: #7b0a0a;
    --ink: #1a1a1a;
    --white: #ffffff;
    --badge-blue: #2a3fe0;
    --badge-blue-soft: #4a5cf0;
    --tick-blue: #1f3fe0;
    --wash-pink: #f7e4e8;
    --wash-lilac: #e9e8f6;
    --paper: #ffffff;
  }
  * { margin: 0; padding: 0; box-sizing: border-box; }
  html, body { width: 850px; height: 1200px; overflow: hidden; background: var(--paper); }
  .flyer {
    position: relative;
    width: 850px;
    height: 1200px;
    overflow: hidden;
    background: var(--paper);
    font-family: "Delius", "Comic Sans MS", sans-serif;
    color: var(--ink);
  }
  .language-backdrop {
    position: absolute;
    left: 0; top: 0;
    width: 850px; height: 950px;
    background: linear-gradient(135deg, var(--wash-lilac) 0%, var(--wash-pink) 50%, var(--wash-lilac) 100%);
    opacity: 0.6;
  }
  .title-panel {
    position: absolute;
    left: 22px; top: 20px;
    width: 806px; height: 210px;
    background: var(--maroon);
    border-radius: 12px;
    color: var(--white);
    text-align: center;
  }
  .title-panel h1 {
    font-family: "Cabin Sketch", "Comic Sans MS", cursive;
    font-weight: 400;
    font-size: 68px;
    letter-spacing: 2px;
    line-height: 1;
    margin-top: 52px;
  }
  .title-panel .tagline {
    font-size: 28px;
    letter-spacing: 0.6px;
    margin-top: 14px;
  }
  .intro {
    position: absolute;
    left: 20px; top: 278px;
    width: 810px;
    text-align: center;
    font-size: 27px;
    letter-spacing: 0.5px;
    line-height: 35px;
  }
  .accent { color: var(--maroon); }
  .intro .accent:first-child { font-size: 29px; }
  .services {
    position: absolute;
    left: 90px; top: 408px;
    list-style: none;
    font-size: 27px;
    letter-spacing: 0.9px;
  }
  .services li {
    display: flex;
    align-items: center;
    height: 53px;
  }
  .services svg { width: 32px; height: 30px; margin-right: 16px; flex: none; }
  .price-badge {
    position: absolute;
    left: 294px; top: 582px;
    width: 260px; height: 260px;
    border-radius: 50%;
    background: radial-gradient(circle at 50% 50%, var(--badge-blue-soft) 0%, var(--badge-blue) 100%);
    display: flex;
    flex-direction: column;
    align-items: center;
    justify-content: center;
    color: var(--white);
    font-family: Arial, Helvetica, sans-serif;
    text-align: center;
    line-height: 1.15;
  }
  .price-badge .amount { font-size: 38px; }
  .price-badge .unit { font-size: 20px; }
  .price-badge .unit.class { font-size: 23px; }
  .group-rates {
    position: absolute;
    left: 0; top: 850px;
    width: 850px;
    text-align: center;
    font-size: 28px;
    letter-spacing: 0.8px;
    line-height: 36px;
  }
  .contact-band {
    position: absolute;
    left: 0; top: 950px;
    width: 850px; height: 250px;
    background: var(--maroon);
    color: var(--white);
  }
  .contact-band .lead {
    position: absolute;
    left: 93px; top: 36px;
    font-size: 31px;
    letter-spacing: 0.6px;
    white-space: nowrap;
  }
  .contact-band .name {
    font-family: "Cabin Sketch", "Comic Sans MS", cursive;
    font-weight: 400;
    font-size: 33px;
    letter-spacing: 1px;
    color: var(--white);
  }
  .contact-line {
    position: absolute;
    left: 90px;
    display: flex;
    align-items: center;
    font-size: 30px;
    white-space: nowrap;
  }
  .contact-line svg { width: 40px; height: 30px; margin-right: 32px; flex: none; }
  .contact-line.phone { top: 117px; letter-spacing: 1.5px; }
  .contact-line.email { top: 172px; font-size: 29px; }
</style>
</head>
<body>
<main class="flyer">
  <div class="language-backdrop" role="img" aria-label="Faint background pattern of the word English written in many world languages"></div>

  <header class="title-panel">
    <h1>English Tutoring</h1>
    <p class="tagline">Learn with Private English Classes</p>
  </header>

  <p class="intro"><span class="accent">Private English Classes</span> with an accredited <span class="accent">TEFL</span><br>(Teaching English as a Foreign Language) tutor with 2<br>years of experience</p>

  <ul class="services">
    <li><svg viewBox="0 0 32 30"><path d="M3 16 L12 25 L29 4" fill="none" stroke="var(--tick-blue)" stroke-width="5" stroke-linecap="round" stroke-linejoin="round"/></svg>Classes for BEGINNERS and ADVANCED students</li>
    <li><svg viewBox="0 0 32 30"><path d="M3 16 L12 25 L29 4" fill="none" stroke="var(--tick-blue)" stroke-width="5" stroke-linecap="round" stroke-linejoin="round"/></svg>Proof Reading Services</li>
    <li><svg viewBox="0 0 32 30"><path d="M3 16 L12 25 L29 4" fill="none" stroke="var(--tick-blue)" stroke-width="5" stroke-linecap="round" stroke-linejoin="round"/></svg>Editing Services</li>
  </ul>

  <div class="price-badge" role="img" aria-label="Decorative price badge: £15 per class">
    <span class="amount">£15</span>
    <span class="unit">PER</span>
    <span class="unit class">CLASS</span>
  </div>

  <p class="group-rates">With group rates for <span class="accent">groups</span><br><span class="accent">of 2-4</span> students!</p>

  <footer class="contact-band">
    <p class="lead">To learn more contact <span class="name">Mona Hargrove BTh</span></p>
    <p class="contact-line phone">
      <svg viewBox="0 0 40 30"><path d="M3 9 Q20 -1 37 9 L35 13 L29 12 L28 8 Q20 5 12 8 L11 12 L5 13 Z" fill="#fff"/><path d="M10 14 L30 14 L35 28 L5 28 Z" fill="#fff"/><g fill="var(--maroon)"><circle cx="15" cy="18" r="1.4"/><circle cx="20" cy="18" r="1.4"/><circle cx="25" cy="18" r="1.4"/><circle cx="14" cy="22" r="1.4"/><circle cx="20" cy="22" r="1.4"/><circle cx="26" cy="22" r="1.4"/><circle cx="13" cy="26" r="1.4"/><circle cx="20" cy="26" r="1.4"/><circle cx="27" cy="26" r="1.4"/></g></svg>
      07812609354
    </p>
    <p class="contact-line email">
      <svg viewBox="0 0 40 30"><rect x="2" y="4" width="36" height="24" fill="none" stroke="#fff" stroke-width="2.5"/><path d="M2 4 L20 18 L38 4 M2 28 L15 14 M38 28 L25 14" fill="none" stroke="#fff" stroke-width="2.5"/></svg>
      monahargroveenglish@quillpost.com
    </p>
  </footer>
</main>
</body>
</html>
```